Business Card Designs

Looking to design a 3.5" x 2" standard business card for our employees.
The design needs to be sleek, simple, and modern. We would like our logo (attached) to be incorporated, but not in that colour, rather an outline of the logo in either gold or silver (whichever looks better).

Modern and Simple is what we are looking for, but be creative in incorporating the logo.

```html
<!DOCTYPE html>
<html lang="en">
<head>
<meta charset="utf-8">
<title>Harbourline Suites — Business Card</title>
<link href="https://fonts.googleapis.com/css2?family=Lato:wght@300;400;700&display=swap" rel="stylesheet">
<style>
  :root {
    --backdrop: #141414;
    --card: #262626;
    --gold: #c9a55c;
    --text-light: #d9d9d9;
    --icon-ink: #2a2a2a;
  }
  * { box-sizing: border-box; margin: 0; padding: 0; }
  html, body { width: 1200px; height: 1122px; overflow: hidden; background: var(--backdrop); }
  body { font-family: "Lato", sans-serif; position: relative; }

  .card {
    position: absolute;
    top: 211px;
    width: 400px;
    height: 700px;
    background: var(--card);
    border-radius: 26px;
    box-shadow: 0 18px 40px rgba(0,0,0,.55);
  }
  .card--front { left: 160px; }
  .card--back { left: 640px; }

  /* brand mark: invented name with one plain square */
  .brand { display: flex; flex-direction: column; align-items: center; color: var(--gold); font-weight: 700; text-transform: uppercase; }
  .brand__square { width: 46px; height: 46px; background: var(--gold); margin-bottom: 18px; }
  .brand__name { letter-spacing: .14em; text-align: center; line-height: 1.35; }

  .card--back .brand { position: absolute; top: 230px; left: 0; right: 0; }
  .card--back .brand__square { width: 120px; height: 120px; margin-bottom: 34px; }
  .card--back .brand__name { font-size: 26px; }

  .card--front .brand { position: absolute; top: 70px; left: 0; right: 0; }
  .card--front .brand__name { font-size: 15px; }

  .person { position: absolute; top: 230px; left: 0; right: 0; text-align: center; }
  .person__name { color: var(--gold); font-weight: 700; font-size: 27px; letter-spacing: .03em; text-transform: uppercase; }
  .person__role { color: var(--text-light); font-weight: 400; font-size: 18px; margin-top: 6px; }
  .person__rule { width: 30px; height: 2px; background: var(--gold); margin: 24px auto 0; }

  .address { position: absolute; top: 340px; left: 0; right: 0; text-align: center; color: var(--text-light); font-weight: 300; font-size: 16px; line-height: 1.6; }

  .contacts { position: absolute; top: 430px; left: 62px; right: 30px; list-style: none; }
  .contacts li { display: flex; align-items: center; height: 38px; color: var(--text-light); font-weight: 300; font-size: 16px; }
  .contact__icon { width: 26px; height: 26px; border-radius: 6px; background: var(--gold); display: flex; align-items: center; justify-content: center; margin-right: 18px; flex: none; }
  .contact__icon svg { width: 16px; height: 16px; }
</style>
</head>
<body>

<section class="card card--front" aria-label="Business card front">
  <div class="brand">
    <span class="brand__square"></span>
    <span class="brand__name">Harbourline Suites</span>
  </div>

  <div class="person">
    <h1 class="person__name">Daniel Reyes</h1>
    <p class="person__role">Founder &amp; CEO</p>
    <div class="person__rule"></div>
  </div>

  <p class="address">48 Lakeview Row<br>Northfield, State 24680</p>

  <ul class="contacts">
    <li>
      <span class="contact__icon"><svg viewBox="0 0 16 16"><path d="M4 2l2 3-1.3 1.2a8 8 0 0 0 5 5L11 10l3 2-1 2.5C7 14 2 9 1.5 3z" fill="var(--icon-ink)"/></svg></span>
      (555) 014-2231
    </li>
    <li>
      <span class="contact__icon"><svg viewBox="0 0 16 16"><rect x="4.5" y="1.5" width="7" height="13" rx="1.2" fill="var(--icon-ink)"/><rect x="6" y="3.5" width="4" height="7" fill="var(--gold)"/></svg></span>
      (555) 014-2232
    </li>
    <li>
      <span class="contact__icon"><svg viewBox="0 0 16 16"><rect x="4" y="1.5" width="8" height="4" fill="var(--icon-ink)"/><rect x="1.5" y="6" width="13" height="6" rx="1" fill="var(--icon-ink)"/><rect x="4" y="10" width="8" height="4.5" fill="var(--icon-ink)" stroke="var(--gold)" stroke-width=".8"/></svg></span>
      (555) 014-2233
    </li>
    <li>
      <span class="contact__icon"><svg viewBox="0 0 16 16"><rect x="1.5" y="3.5" width="13" height="9" fill="var(--icon-ink)"/><path d="M1.5 3.5L8 9l6.5-5.5" fill="none" stroke="var(--gold)" stroke-width="1.2"/></svg></span>
      hello@harbourline.example
    </li>
    <li>
      <span class="contact__icon"><svg viewBox="0 0 16 16"><circle cx="8" cy="8" r="6.5" fill="var(--icon-ink)"/><path d="M1.5 8h13M8 1.5c-3 3.5-3 9.5 0 13M8 1.5c3 3.5 3 9.5 0 13" fill="none" stroke="var(--gold)" stroke-width=".9"/></svg></span>
      www.harbourline.example
    </li>
  </ul>
</section>

<section class="card card--back" aria-label="Business card back">
  <div class="brand">
    <span class="brand__square"></span>
    <span class="brand__name">Harbourline<br>Suites</span>
  </div>
</section>

</body>
</html>
```